Web design for Velvet meeting rooms

i would like a classy, elegant website designed for a speed dating events business I am in the progress of starting. I have a logo an would like the webpage to look very sophisticated as I my target market it upper class.
* website needs to be able to be coded easily! thanks

my contact details are:

Email hello@velvetmeetingrooms.com.au
Business number 08 7162 4035
Mobile number 0419275063

I would like to have a feature of upcoming speed dating events as i book them listed on my webpage ( an example of this is http://www.brightcorners.com.au/speed-dating-adelaide-singles) and on this same website is a contact details form to the right where clients will be filling in their details to forward to me.. Is this possible to have on my website through this process? Also I am looking to have paymoor payment options?

Business information

Velvet Meeting Rooms
Adelaide CBD, Australia

Velvet meeting rooms is an elegant and sophisticated speed dating organisation. New to Adelaide, we aim to provide a service where you feel pampered and have fun while ‘dating’ with a touch of class! With extensive dating industry experience in Adelaide and North America, founder Lorinda Pask, has a passion for introducing singles. So, let’s get out there and date with speed! Your soul mate could be at the next table!

more text to come
Updates

Project Deadline Extended
Reason: Still need changes and designs submitted, also wanting to discuss coding options with designers. I have a domain name and serve otter account set up.

Industry/Entity Type

Dating

```html
<!DOCTYPE html>
<html lang="en">
<head>
<meta charset="utf-8">
<title>Velvet Meeting Rooms</title>
<link rel="stylesheet" href="https://fonts.googleapis.com/css2?family=Open+Sans:wght@300;400;600&display=swap">
<style>
:root{
  --black:#0d0c0b;
  --gold:#b8903c;
  --gold-light:#e3c77d;
  --gold-dark:#8e6a24;
  --orange:#c8702a;
  --grey-bg:#e2e2e2;
  --text:#3d3d3d;
  --muted:#6a6a6a;
  --line:#e3e3e3;
  --white:#fff;
}
*{margin:0;padding:0;box-sizing:border-box}
html,body{width:1200px;height:900px;overflow:hidden;background:var(--white);font-family:"Open Sans",Arial,sans-serif;color:var(--text)}
.page{position:absolute;left:277px;top:0;width:646px;height:900px}
.abs{position:absolute}
.abs,.abs *{white-space:nowrap}

/* header */
.site-header{left:0;top:0;width:646px;height:65px;background:var(--black)}
.header-tab{left:0;top:0;width:646px;height:80px}
.brand{left:263px;top:24px;width:120px;text-align:center}
.brand-name{font-size:11px;font-weight:400;color:var(--gold-light);letter-spacing:.5px;line-height:14px}
.brand-rule{margin:4px auto 0;width:92px;height:1px;background:var(--gold)}
.header-contact{left:437px;top:24px;font-size:7px;color:var(--gold);line-height:14px}
.header-contact div{display:flex;align-items:center;gap:7px}
.icon-dot{width:9px;height:9px;border-radius:50%;background:var(--gold);display:inline-block}

/* hero */
.hero{left:0;top:65px;width:646px;height:261px;background:linear-gradient(90deg,#c8a25e 0%,#8a6a3d 35%,#2a221c 58%,#8e6a48 75%,#3a3431 100%)}
.hero-copy{left:85px;top:125px;color:var(--white)}
.hero-line1{font-size:15px;font-weight:300}
.hero-line1 b{font-weight:400}
.hero-line2{font-size:23px;font-weight:300;margin-top:-5px}
.hero-line2 b{font-weight:400}
.hero-button{left:85px;top:184px;width:161px;height:25px;background:rgba(40,32,26,.75);border:1px solid rgba(255,255,255,.3);color:var(--white);font-size:12px;font-weight:300;line-height:23px;text-align:center;white-space:nowrap}

/* about */
.about{left:0;top:326px;width:646px;height:192px;background:var(--grey-bg)}
.about-title{left:85px;top:352px;font-size:15px;font-weight:300;color:var(--gold)}
.about-text{left:85px;top:385px;width:275px;font-size:7.8px;line-height:15px;color:var(--text);text-align:justify}
.about-text,.about-text *{white-space:normal}
.about-photo{border-radius:50%;border:3px solid var(--white)}

/* events */
.events{left:0;top:518px;width:646px;height:345px;background:linear-gradient(180deg,#3c2412 0%,#7a4a22 45%,#5a3516 75%,#2a1a0e 100%)}
.ribbon{left:225px;top:499px}
.events-table{left:84px;top:559px;width:290px;height:272px;background:var(--white);font-size:6.5px}
.table-head{height:24px;border-bottom:1px solid var(--line);color:var(--gold);font-size:8px;line-height:24px;position:relative}
.table-row{height:50px;border-bottom:1px solid var(--line);position:relative;line-height:9.5px;color:var(--muted)}
.table-row:last-child{border-bottom:0}
.col{position:absolute}
.c-event{left:41px}.c-date{left:121px}.c-age{left:175px}.c-status{left:213px}.c-price{left:260px}
.table-head .c-event{left:6px}
.table-row .col{top:11px}
.thumb{position:absolute;left:5px;top:10px;width:30px;height:30px;border-radius:3px;background:linear-gradient(135deg,#6b4a2c,#c09a6a)}
.event-name{color:#555;font-weight:600;font-size:6.3px}
.status{color:var(--orange)}

/* form */
.suggest-form{left:403px;top:559px;width:158px;height:272px;background:var(--white);font-size:6.5px}
.form-head{height:24px;border-bottom:1px solid var(--line);color:var(--gold-dark);font-size:8px;line-height:24px;padding-left:7px}
.form-intro{left:7px;top:30px;width:140px;line-height:9px;color:var(--text);font-size:6.2px}
.form-intro,.form-intro *{white-space:normal}
.field-label{right:90px;width:70px;text-align:right;color:var(--orange);font-size:6.8px;line-height:12px}
.field{left:71px;width:81px;height:12px;border:1px solid #cfcfcf;background:#f2f2f2;color:var(--muted);font-size:5.5px;line-height:10px;padding-left:3px;overflow:hidden}
.field.select::after{content:"";position:absolute;right:3px;top:4px;border:2px solid transparent;border-top:3px solid #888}
.field-and{font-size:6.5px;color:var(--text);line-height:12px}
.suggest-button{left:7px;top:242px;width:145px;height:23px;background:linear-gradient(180deg,#e8d08e,#bf9a4c);color:var(--gold-dark);font-size:9.5px;line-height:23px;text-align:center;border-radius:2px}

/* footer */
.site-footer{left:0;top:863px;width:646px;height:37px;background:var(--grey-bg);font-size:5.5px;color:var(--muted);line-height:37px}
.footer-left{left:85px}
.footer-right{left:359px}
</style>
</head>
<body>
<div class="page">
  <header class="abs site-header"></header>
  <svg class="abs header-tab" width="646" height="80" viewBox="0 0 646 80" aria-hidden="true">
    <path d="M0 65 H200 L215 78 H431 L446 65 H646" fill="none" stroke="#4a4238" stroke-width="1"/>
    <path d="M200 64 L215 78 H431 L446 64 Z" fill="#0d0c0b"/>
  </svg>
  <div class="abs brand">
    <div class="brand-name">VELVET MEETING ROOMS</div>
    <div class="brand-rule"></div>
  </div>
  <div class="abs header-contact">
    <div><span class="icon-dot"></span>08 7162 4035 - 0419275063</div>
    <div><span class="icon-dot"></span>hello@velvetmeetingrooms.com.au</div>
  </div>

  <section class="abs hero" role="img" aria-label="Photo of a smiling couple toasting with red wine in an elegant restaurant"></section>
  <div class="abs hero-copy">
    <div class="hero-line1">Have fun while <b>dating</b></div>
    <div class="hero-line2">with a touch of <b>class</b></div>
  </div>
  <div class="abs hero-button">Check out upcoming events</div>

  <section class="abs about"></section>
  <h2 class="abs about-title">Your soul mate could be at the next table</h2>
  <p class="abs about-text">Velvet meeting rooms is a elegant and sophisticated speed dating organisation. New to Adelaide we aim to provide a service where you can feel good and have fun while dating with a touch of class! Founder Lorinda Pask has had extensive experience in Adelaide and North America in the dating industry and has a passion for introducing singles. Lets get out there and date with speed! Your soul mate could be at the next table.</p>
  <div class="abs about-photo" style="left:398px;top:351px;width:90px;height:90px;background:radial-gradient(circle,#a77a4c,#4a2e1a)" role="img" aria-label="Photo of a couple sharing wine at dinner"></div>
  <div class="abs about-photo" style="left:473px;top:384px;width:86px;height:86px;background:radial-gradient(circle,#6e6a70,#2a2a30)" role="img" aria-label="Photo of a well-dressed couple embracing"></div>
  <div class="abs about-photo" style="left:423px;top:421px;width:63px;height:63px;background:radial-gradient(circle,#d8b07a,#5e3a1c)" role="img" aria-label="Photo of a warmly lit restaurant interior"></div>

  <section class="abs events" role="img" aria-label="Photo of a candlelit restaurant dining room"></section>
  <svg class="abs ribbon" width="186" height="34" viewBox="0 0 186 34" aria-hidden="true">
    <defs><linearGradient id="ribbonGold" x1="0" y1="0" x2="0" y2="1"><stop offset="0" stop-color="#e5cd8a"/><stop offset="1" stop-color="#b48c40"/></linearGradient></defs>
    <path d="M0 9 H40 V30 H0 L10 19.5 Z" fill="#a9843a"/>
    <path d="M186 9 H146 V30 H186 L176 19.5 Z" fill="#a9843a"/>
    <rect x="33" y="2" width="120" height="24" fill="url(#ribbonGold)"/>
    <text x="93" y="18" text-anchor="middle" font-family="Open Sans, Arial, sans-serif" font-size="9" fill="#7a5a1e">UPCOMING EVENTS</text>
  </svg>

  <div class="abs events-table">
    <div class="table-head">
      <span class="col c-event">Event type &amp; city</span>
      <span class="col c-date">Date &amp; Time</span>
      <span class="col c-age">Age</span>
      <span class="col c-status">Status</span>
      <span class="col c-price">Price</span>
    </div>
    <div class="table-row"><div class="thumb" role="img" aria-label="Venue photo"></div>
      <div class="col c-event"><span class="event-name">Speed dating with style</span><br>Laurel Dining Room<br>Adelaide</div>
      <div class="col c-date">04.26.2014<br>7.00pm</div><div class="col c-age">M : 40-50<br>F : 35-42</div>
      <div class="col c-status status">2 spaces left</div><div class="col c-price">$ 95.20</div></div>
    <div class="table-row"><div class="thumb" role="img" aria-label="Venue photo"></div>
      <div class="col c-event"><span class="event-name">Tall men speed dating</span><br>The Ashgrove Hotel<br>Adelaide</div>
      <div class="col c-date">05.03.2014<br>10.00pm</div><div class="col c-age">M : 30-40<br>F : 25-35</div>
      <div class="col c-status status">1 spaces left</div><div class="col c-price">$ 87.15</div></div>
    <div class="table-row"><div class="thumb" role="img" aria-label="Venue photo"></div>
      <div class="col c-event"><span class="event-name">Single's party</span><br>Bar 27, Eastside<br>Adelaide</div>
      <div class="col c-date">04.26.2014<br>7.00pm</div><div class="col c-age">M : 40-50<br>F : 35-42</div>
      <div class="col c-status status">2 spaces left</div><div class="col c-price">$ 95.20</div></div>
    <div class="table-row"><div class="thumb" role="img" aria-label="Venue photo"></div>
      <div class="col c-event"><span class="event-name">Speed dating with style</span><br>Laurel Dining Room<br>Adelaide</div>
      <div class="col c-date">04.26.2014<br>7.00pm</div><div class="col c-age">M : 40-50<br>F : 35-42</div>
      <div class="col c-status status">2 spaces left</div><div class="col c-price">$ 95.20</div></div>
    <div class="table-row"><div class="thumb" role="img" aria-label="Venue photo"></div>
      <div class="col c-event"><span class="event-name">Speed dating with style</span><br>Laurel Dining Room<br>Adelaide</div>
      <div class="col c-date">04.26.2014<br>7.00pm</div><div class="col c-age">M : 40-50<br>F : 35-42</div>
      <div class="col c-status status">2 spaces left</div><div class="col c-price">$ 95.20</div></div>
  </div>

  <form class="abs suggest-form">
    <div class="form-head">Let us know you for a perfect event</div>
    <p class="abs form-intro">Tell us a bit about yourself to see speed dating &amp; singles events that suit you. It's free !</p>
    <span class="abs field-label" style="top:64px">Name &amp; Surname :</span><span class="abs field" style="top:64px"></span>
    <span class="abs field-label" style="top:82px">Birth date :</span>
    <span class="abs field select" style="top:82px;width:22px">MM</span>
    <span class="abs field select" style="top:82px;left:96px;width:22px">DD</span>
    <span class="abs field select" style="top:82px;left:121px;width:31px">YY</span>
    <span class="abs field-label" style="top:100px">I live in :</span><span class="abs field select" style="top:100px">Please select one</span>
    <span class="abs field-label" style="top:118px">I am a :</span><span class="abs field select" style="top:118px">Please select one</span>
    <span class="abs field-label" style="top:136px">Aged between :</span>
    <span class="abs field select" style="top:136px;width:33px">Select</span>
    <span class="abs field-and" style="left:107px;top:136px">and</span>
    <span class="abs field select" style="top:136px;left:120px;width:32px">Select</span>
    <span class="abs field-label" style="top:154px">My education level :</span><span class="abs field select" style="top:154px">Please select one</span>
    <span class="abs field-label" style="top:172px">I am a :</span><span class="abs field select" style="top:172px">Please select one</span>
    <span class="abs field-label" style="top:192px">My height is :</span><span class="abs field select" style="top:192px">Please select one</span>
    <span class="abs field-label" style="top:210px">Email :</span><span class="abs field" style="top:210px"></span>
    <div class="abs suggest-button">SUGGEST ME AN EVENT</div>
  </form>

  <footer class="abs site-footer">
    <span class="abs footer-left">© 2014 Velvet Meeting Rooms | All rights reserved</span>
    <span class="abs footer-right">Phone : 08 7162 4035 - 0419275063 &nbsp;&nbsp; Email : hello@velvetmeetingrooms.com.au</span>
  </footer>
</div>
</body>
</html>
```